Paw Summit Co business card

I need a business card design for a dog training company in Toronto called Paw Summit Co. My training is unique, outdoor training that helps people create a better bond with their dog through communication and understanding their dog's true nature. I do not use treats - but communication and praise for the dog.

I help people create a better life for them and their dog. From puppy training right through to seniors, I offer both group classes called Curbside Poise Course as well as in-home private sessions.

I believe that having a dog is a lifestyle, so I encourage clients to incorporate their dog into their active life. Outdoor activities such as hiking, mental stimulation, proper care and healthy food for their dog are all keys to a healthy and happy dog.

I would like a fresh and modern look that works with my logo. I would like to convey fun, confidence and happiness.

My services are premium services. I am a Certified Dog Trainer, and offer value for money, but my prices are higher than other trainers.
Updates

Thank you to everyone who submitted designs! I'm so impressed with the level of creativity and the options that you all have given me. It will be a difficult choice for sure. As this was my first experience with Art Huddle - it has been a great one.

maren.

Industry/Entity Type

Communication

Requirements
Must have
• Maren Quill, CTE
Certified Trainer Educator
maren@pawsummitco.ca
555-318-0472
pawsummitco.ca

Prefer a double sided card.
Must have Paw Summit Co logo. File attached. I do have a stroke logo for a dark background as well.

Must only use the fonts and colours as outlined in my brand guidelines, which are attached.
Should not have
• no cheesy pet images
do not use the tongue as an element outside of the logo
minimize the use of pink - can be used as an accent colour but should not be a main colour

```html
<!DOCTYPE html>
<html lang="en">
<head>
<meta charset="utf-8">
<title>Paw Summit Co — Business Card</title>
<link href="https://fonts.googleapis.com/css2?family=Tinos:wght@400;700&display=swap" rel="stylesheet">
<style>
  :root {
    --backdrop: #8f8f8f;
    --card-blue: #33b5ee;
    --ink: #1c1c1c;
    --lime: #8fdc2b;
    --edge: #3a3a3a;
  }
  * { margin: 0; padding: 0; box-sizing: border-box; }
  html, body {
    width: 1200px;
    height: 1194px;
    overflow: hidden;
  }
  body {
    position: relative;
    background: var(--backdrop);
    font-family: "Tinos", "Times New Roman", serif;
    color: var(--ink);
  }
  .card {
    position: absolute;
    width: 834px;
    height: 476px;
    background: var(--card-blue);
    border: 1.5px solid var(--edge);
    overflow: hidden;
  }
  .card--front { left: 59px; top: 138px; }
  .card--back  { left: 324px; top: 656px; }

  /* Front: wordmark */
  .front-mark {
    position: absolute;
    left: 40px;
    top: 170px;
    display: flex;
    align-items: center;
    gap: 22px;
  }
  .front-mark__dot {
    flex: none;
    width: 72px;
    height: 72px;
    border-radius: 50%;
    background: var(--lime);
  }
  .front-mark__name {
    font-weight: 700;
    font-size: 86px;
    line-height: 1;
    letter-spacing: -1px;
    color: var(--ink);
    white-space: nowrap;
  }

  /* Back: rule line and small wordmark */
  .rule {
    position: absolute;
    top: 103px;
    height: 4px;
    background: var(--ink);
  }
  .rule--lead  { left: 0; width: 66px; }
  .rule--main  { left: 264px; width: 505px; }
  .rule--tail  { left: 788px; width: 46px; }
  .back-mark {
    position: absolute;
    left: 74px;
    top: 88px;
    font-weight: 700;
    font-size: 26px;
    line-height: 1;
    color: var(--ink);
    white-space: nowrap;
  }

  .contact {
    position: absolute;
    right: 68px;
    top: 160px;
    text-align: right;
  }
  .contact__name {
    font-weight: 400;
    font-size: 50px;
    line-height: 1.12;
  }
  .contact__credential {
    font-size: 30px;
    letter-spacing: 1px;
  }
  .contact__line {
    font-weight: 700;
    font-size: 35px;
    line-height: 1.22;
  }
</style>
</head>
<body>
  <section class="card card--front" aria-label="Card front">
    <div class="front-mark">
      <span class="front-mark__dot"></span>
      <span class="front-mark__name">Paw Summit Co</span>
    </div>
  </section>

  <section class="card card--back" aria-label="Card back">
    <span class="rule rule--lead"></span>
    <span class="back-mark">Paw Summit Co</span>
    <span class="rule rule--main"></span>
    <span class="rule rule--tail"></span>

    <div class="contact">
      <p class="contact__name">Maren Quill,<span class="contact__credential">CTE</span></p>
      <p class="contact__line">Certified Trainer Educator</p>
      <p class="contact__line">Pawsummitco.ca</p>
      <p class="contact__line">maren@pawsummitco.ca</p>
      <p class="contact__line">555.318.0472</p>
    </div>
  </section>
</body>
</html>
```